Bref créative
Business Card and Stationery for Voice and Data Company
Looking for a high tech and modern design
Use same font as used in my logo
See supplied artwork
Professional
Owen Castellan
Owner
P.O. Box 4382 Broomfield, CO 80049
Owen@qvlinkgrid.com
www.qvlinkgrid.com
On the back of the business card, we would like to see a few different drafts:
1) Include Zentro and Bx&q logos and text listed in the Back of the business card section:
2) Include our logo, url of our website, and the text in the back of the business card section
3) Include picture of digital phone, the text in the back of the business card section, our logo, and url to our website
4) Any combination of the drafts above. Feel free to be creative.
We want the following services as bullet points:
Voice and Data Solutions
Structured Cabling
IP Surveillance Cameras

```html
<!DOCTYPE html>
<html lang="en">
<head>
<meta charset="utf-8">
<title>QV Link Grid Stationery</title>
<link href="https://fonts.googleapis.com/css2?family=Open+Sans:wght@400;700;800&display=swap" rel="stylesheet">
<style>
:root{
  --bg:#ebe6de;
  --paper:#ffffff;
  --blue:#2c6aa3;
  --blue-dark:#1d4c7a;
  --blue-light:#6fa3d2;
  --green:#6aaa3f;
  --ink:#3c3c3c;
  --muted:#8a8a8a;
  --grey:#8f9396;
  --grey-dark:#5f6366;
  --label:#6c6257;
}
*{box-sizing:border-box;margin:0;padding:0}
html,body{width:1200px;height:446px;overflow:hidden}
body{background:var(--bg);font-family:"Open Sans",Arial,sans-serif;color:var(--ink);position:relative}
.piece{position:absolute;background:var(--paper);box-shadow:0 1px 4px rgba(0,0,0,.25);overflow:hidden}
.piece svg.decor{position:absolute;inset:0;width:100%;height:100%}
.label{position:absolute;font-size:5px;letter-spacing:.8px;color:var(--label);text-transform:uppercase;white-space:nowrap}
.brand{position:absolute;display:flex;align-items:center;gap:4px;font-weight:800;color:var(--green);line-height:1;white-space:nowrap}
.brand .mark{background:var(--blue);display:block;flex:none}
.contact{position:absolute;font-size:4px;line-height:6px;color:var(--muted);white-space:nowrap}
.contact .dot{display:inline-block;width:3px;height:3px;border-radius:50%;background:var(--blue);margin-right:2px;vertical-align:middle}

/* business cards */
.card-front{left:10px;top:90px;width:106px;height:58px}
.card-front .person{position:absolute;left:5px;top:8px;color:#fff;font-size:3.5px;line-height:5px;white-space:nowrap}
.card-front .person strong{display:block;font-size:4.5px;font-weight:700}
.card-front .brand{right:5px;top:22px;font-size:5.5px;gap:3px}
.card-front .brand .mark{width:6px;height:6px}
.card-back{left:10px;top:170px;width:106px;height:56px;background:var(--blue)}
.card-back .brand{left:8px;top:22px;font-size:6px}
.card-back .brand .mark{width:9px;height:9px;background:#fff}

/* letterheads */
.letter-one{left:150px;top:8px;width:300px;height:428px}
.letter-one .brand{left:18px;top:20px;font-size:11px}
.letter-one .brand .mark{width:13px;height:13px}
.letter-one .contact{left:208px;top:18px}
.letter-two{left:474px;top:8px;width:308px;height:428px}
.letter-two .brand{left:100px;top:24px;font-size:11px}
.letter-two .brand .mark{width:13px;height:13px}
.letter-two .watermark{position:absolute;left:104px;top:120px;width:100px;height:100px;background:var(--blue-light);opacity:.15}
.letter-two .contact{left:110px;top:402px}

/* envelopes */
.env-one{left:806px;top:0;width:394px;height:128px}
.env-two{left:806px;top:136px;width:394px;height:92px}
.env-two .brand{left:170px;top:60px;font-size:7px}
.env-two .brand .mark{width:8px;height:8px}
.env-three{left:806px;top:236px;width:394px;height:74px}
.env-front{left:798px;top:320px;width:402px;height:118px}
.env-front .brand{left:36px;top:18px;font-size:9px}
.env-front .brand .mark{width:11px;height:11px}
.env-front .contact{left:36px;top:34px}
.env-front .watermark{position:absolute;right:40px;top:18px;width:72px;height:72px;background:var(--blue-light);opacity:.15}
</style>
</head>
<body>

<span class="label" style="left:10px;top:80px">Business Card Front</span>
<div class="piece card-front">
  <svg class="decor" viewBox="0 0 106 58" preserveAspectRatio="none">
    <path d="M0 0H54C44 18 54 40 40 58H0Z" fill="var(--blue)"/>
    <path d="M54 0C44 18 54 40 40 58" stroke="var(--blue-light)" stroke-width="1.2" fill="none"/>
  </svg>
  <div class="person"><strong>Owen Castellan</strong>Owner</div>
  <div class="brand"><span class="mark"></span>QV Link Grid</div>
</div>
<span class="label" style="left:10px;top:155px">Business Card Back</span>
<div class="piece card-back">
  <div class="brand" style="color:#fff"><span class="mark"></span>QV Link Grid</div>
</div>

<div class="piece letter-one">
  <svg class="decor" viewBox="0 0 300 428" preserveAspectRatio="none">
    <path d="M0 370C90 410 200 340 300 390V428H0Z" fill="var(--blue)"/>
    <path d="M0 360C90 400 200 330 300 380" stroke="var(--blue-light)" stroke-width="1.5" fill="none"/>
  </svg>
  <div class="brand"><span class="mark"></span>QV Link Grid, Inc.</div>
  <div class="contact">
    <div><span class="dot"></span>303-555-0147</div>
    <div><span class="dot"></span>P.O. Box 4382 Broomfield, CO 80049</div>
    <div><span class="dot"></span>Owen@qvlinkgrid.com</div>
    <div><span class="dot"></span>www.qvlinkgrid.com</div>
  </div>
</div>
<span class="label" style="left:260px;top:439px">Letterhead Option 1</span>

<div class="piece letter-two">
  <svg class="decor" viewBox="0 0 308 428" preserveAspectRatio="none">
    <path d="M0 0H30C10 140 40 300 8 428H0Z" fill="var(--blue)"/>
    <path d="M34 0C14 140 44 300 12 428" stroke="var(--blue-light)" stroke-width="1.5" fill="none"/>
  </svg>
  <div class="brand"><span class="mark"></span>QV Link Grid, Inc.</div>
  <div class="watermark" role="img" aria-label="Faint background shape"></div>
  <div class="contact">P.O. Box 4382 Broomfield, CO 80049 · www.qvlinkgrid.com</div>
</div>
<span class="label" style="left:590px;top:439px">Letterhead Option 2</span>

<div class="piece env-one">
  <svg class="decor" viewBox="0 0 394 128" preserveAspectRatio="none">
    <path d="M0 0H394V30C300 60 120 20 0 50Z" fill="var(--blue)"/>
  </svg>
</div>
<div class="piece env-two">
  <svg class="decor" viewBox="0 0 394 92" preserveAspectRatio="none">
    <path d="M0 0H394V22L220 56Q197 60 174 56L0 22Z" fill="var(--grey-dark)"/>
  </svg>
  <div class="brand"><span class="mark"></span>QV Link Grid</div>
</div>
<div class="piece env-three">
  <svg class="decor" viewBox="0 0 394 74" preserveAspectRatio="none">
    <path d="M0 14L174 48Q197 52 220 48L394 14" stroke="var(--grey)" stroke-width="1" fill="none"/>
  </svg>
</div>
<div class="piece env-front">
  <svg class="decor" viewBox="0 0 402 118" preserveAspectRatio="none">
    <path d="M0 0H20C8 40 22 80 60 100C160 118 300 96 402 110V118H0Z" fill="var(--blue)"/>
  </svg>
  <div class="brand"><span class="mark"></span>QV Link Grid, Inc.</div>
  <div class="contact">P.O. Box 4382<br>Broomfield, CO 80049</div>
  <div class="watermark" role="img" aria-label="Faint background shape"></div>
</div>
<span class="label" style="left:1000px;top:312px">Envelope Option 1</span>

</body>
</html>
```